STATIONARY PACK FOR LOADMARK
Business Cards, Email Footer, A4 Presentation Folder, Letterhead etc
Project: STATIONARY PACK FOR LOADMARK
STATIONARY PACK FOR LOADMARK - Construction
Creative Brief
Simple
Colin Bradshaw
General Manager
Level 3 248Harbour Road Auckland 1010
colin@loadmark.example.nz
www.loadmark.example.nz
Please ensure you make the following as part of this design package, Email footer, Business Card Double Sided, Letterhead, A4 Presentation folder.
loadmark.example.nz in the bottom left corner Solid Colour Matt Finish "Your one stop Hire Shop"

```html
<!DOCTYPE html>
<html lang="en">
<head>
<meta charset="utf-8">
<title>LOADMARK Business Card</title>
<link href="https://fonts.googleapis.com/css2?family=Raleway:wght@400;500;600;700&display=swap" rel="stylesheet">
<style>
  :root {
    --navy: #3b4160;
    --orange: #f0653b;
    --ink: #2c2f3a;
    --muted: #7a7d88;
    --rule: #c9cbd2;
    --card: #ffffff;
    --backdrop: #e4e5e8;
  }
  * { box-sizing: border-box; margin: 0; padding: 0; }
  html, body { width: 1200px; height: 902px; overflow: hidden; }
  body {
    background: var(--backdrop);
    font-family: "Raleway", sans-serif;
    color: var(--ink);
    display: flex;
    flex-direction: column;
    align-items: center;
    justify-content: center;
    gap: 56px;
  }
  .card {
    position: relative;
    width: 640px;
    height: 366px;
    background: var(--card);
    border-radius: 14px;
    overflow: hidden;
    box-shadow: 0 10px 30px rgba(0,0,0,0.12);
  }
  .brand-name {
    font-weight: 700;
    color: var(--navy);
    letter-spacing: 1px;
    line-height: 1;
    white-space: nowrap;
  }
  /* Back side */
  .card-back {
    display: flex;
    align-items: center;
    justify-content: center;
  }
  .card-back .brand-name { font-size: 52px; }
  /* Front side */
  .brand-block {
    position: absolute;
    left: 34px;
    top: 100px;
  }
  .brand-block .brand-name { font-size: 44px; }
  .divider {
    position: absolute;
    left: 392px;
    top: 52px;
    width: 1px;
    height: 190px;
    background: var(--rule);
  }
  .contact-block {
    position: absolute;
    left: 412px;
    top: 58px;
  }
  .person-name { font-size: 17px; font-weight: 600; color: var(--ink); }
  .person-title {
    font-size: 8px;
    letter-spacing: 1.2px;
    color: var(--muted);
    text-transform: uppercase;
    margin-top: 3px;
  }
  .contact-list { list-style: none; margin-top: 34px; }
  .contact-list li {
    display: flex;
    align-items: center;
    gap: 8px;
    font-size: 9px;
    color: var(--muted);
    height: 18px;
    white-space: nowrap;
  }
  .contact-list svg { width: 9px; height: 9px; fill: var(--orange); flex: none; }
  .card-wave {
    position: absolute;
    left: 0;
    bottom: 0;
    width: 640px;
    height: 120px;
  }
</style>
</head>
<body>
  <section class="card card-back">
    <div class="brand-name">LOADMARK</div>
  </section>

  <section class="card card-front">
    <div class="brand-block">
      <div class="brand-name">LOADMARK</div>
    </div>
    <div class="divider"></div>
    <div class="contact-block">
      <div class="person-name">Colin Bradshaw</div>
      <div class="person-title">Managing Director</div>
      <ul class="contact-list">
        <li><svg viewBox="0 0 10 10"><path d="M2 0h2l1 3-1.5 1a6 6 0 0 0 2.5 2.5L7 5l3 1v2a2 2 0 0 1-2 2A8 8 0 0 1 0 2a2 2 0 0 1 2-2z"/></svg>012 345 6789</li>
        <li><svg viewBox="0 0 10 10"><rect x="2.5" y="0" width="5" height="10" rx="1"/></svg>012 345 6789</li>
        <li><svg viewBox="0 0 10 10"><rect x="1" y="2" width="8" height="6" rx="1"/></svg>012 345 6789</li>
        <li><svg viewBox="0 0 10 10"><path d="M0 2h10v6H0z"/></svg>colin@loadmark.example.nz</li>
        <li><svg viewBox="0 0 10 10"><circle cx="5" cy="5" r="4.5"/></svg>www.loadmark.example.nz</li>
      </ul>
    </div>
    <svg class="card-wave" viewBox="0 0 640 120" preserveAspectRatio="none">
      <path d="M0 44 C180 20 360 40 640 78" fill="none" stroke="var(--orange)" stroke-width="5"/>
      <path d="M0 58 C180 34 360 54 640 92 L640 120 L0 120 Z" fill="var(--navy)"/>
    </svg>
  </section>
</body>
</html>
```